Quorvane Capital Modern Business Card

We need a modern business card template designed for Quorvane Capital.
Quorvane Capital is a diversified global cryptocurrency investment fund.

The font under the logo: Hiragino Kaku Gothic Pro

Color Hexcode: Main colors white (ffffff) & teal (188383), we are open to adding #fcca46 as an accent

Target Market(s)

Accredited Investors, high net worth individuals and institutional investors

Industry/Entity Type

Investment

Contact Information for Business Card

Contact Information should contain
Name
main phone +1 720 555 0147
cell
email

Font styles to use
Sans Serif
Other font styles liked:
• Hiragino Kaku Gothic Pro

Requirements
Must have
• would like to have icons that identify the contact information
• include our website: www.quorvanecapital.example
• include our Tagline: Diversified Crypto Investment Funds
Nice to have
• Would like to have a simple back side with the logo (without the words) and plenty of space

```html
<!DOCTYPE html>
<html lang="en">
<head>
<meta charset="utf-8">
<title>Quorvane Capital — Business Card</title>
<link href="https://fonts.googleapis.com/css2?family=Noto+Sans+JP:wght@400;500&family=Open+Sans:ital,wght@0,400;0,600;0,700;1,700&display=swap" rel="stylesheet">
<style>
  :root {
    --backdrop: #e8e5e0;
    --card-white: #ffffff;
    --card-black: #050505;
    --teal: #188383;
    --accent: #fcca46;
    --ink: #1e1e1e;
    --ink-soft: #3a3a3a;
  }
  * { margin: 0; padding: 0; box-sizing: border-box; }
  html, body {
    width: 1200px;
    height: 800px;
    overflow: hidden;
    background: var(--backdrop);
  }
  .canvas {
    position: relative;
    width: 1200px;
    height: 800px;
    display: flex;
    align-items: center;
    justify-content: center;
    gap: 40px;
  }
  .card {
    position: relative;
    width: 540px;
    height: 320px;
    border-radius: 3px;
    box-shadow: 0 8px 24px rgba(0,0,0,0.14);
    overflow: hidden;
  }

  /* Back side */
  .card-back {
    background: var(--card-black);
    display: flex;
    align-items: center;
    justify-content: center;
  }
  .back-name {
    font-family: "Noto Sans JP", sans-serif;
    font-weight: 500;
    font-size: 20px;
    letter-spacing: 2px;
    text-transform: uppercase;
    color: var(--teal);
  }

  /* Front side */
  .card-front {
    background: var(--card-white);
    font-family: "Open Sans", sans-serif;
    color: var(--ink);
  }
  .name-block {
    position: absolute;
    left: 26px;
    top: 28px;
    padding-left: 14px;
    border-left: 6px solid var(--accent);
  }
  .person-name {
    font-weight: 700;
    font-size: 21px;
    line-height: 1.1;
    letter-spacing: 0.5px;
  }
  .person-role {
    font-size: 13px;
    color: var(--ink-soft);
  }
  .company-info {
    position: absolute;
    left: 32px;
    top: 132px;
  }
  .website {
    font-size: 13.5px;
    color: var(--ink-soft);
  }
  .tagline {
    font-size: 13px;
    font-weight: 700;
    font-style: italic;
    margin-top: 2px;
  }
  .contact {
    position: absolute;
    display: flex;
    flex-direction: column;
    align-items: flex-start;
    font-size: 13px;
    color: var(--ink-soft);
  }
  .contact-icon {
    width: 24px;
    height: 24px;
    border-radius: 50%;
    background: var(--teal);
    display: flex;
    align-items: center;
    justify-content: center;
    margin-bottom: 8px;
  }
  .contact-icon svg { width: 13px; height: 13px; }
  .contact-phone { left: 32px; top: 198px; }
  .contact-phone .contact-icon { margin-left: 22px; }
  .contact-email { left: 190px; top: 226px; }
  .contact-email .contact-icon { margin-left: 76px; }
  .contact-mobile { left: 388px; top: 254px; }
  .contact-mobile .contact-icon { margin-left: 46px; }

  .brand {
    position: absolute;
    right: 30px;
    top: 120px;
    display: flex;
    align-items: center;
    gap: 10px;
  }
  .brand-square {
    width: 16px;
    height: 16px;
    background: var(--teal);
  }
  .brand-name {
    font-family: "Noto Sans JP", sans-serif;
    font-weight: 400;
    font-size: 19px;
    letter-spacing: 1px;
    text-transform: uppercase;
    color: var(--ink);
  }
  .accent-band {
    position: absolute;
    right: 0;
    bottom: 0;
    width: 170px;
    height: 9px;
  }
</style>
</head>
<body>
  <main class="canvas">
    <section class="card card-back" aria-label="Card back">
      <span class="back-name">Quorvane Capital</span>
    </section>

    <section class="card card-front" aria-label="Card front">
      <div class="name-block">
        <p class="person-name">JOHN DOE</p>
        <p class="person-role">Manager</p>
      </div>

      <div class="company-info">
        <p class="website">www.quorvanecapital.example</p>
        <p class="tagline">Diversified Crypto Investment Funds</p>
      </div>

      <div class="contact contact-phone">
        <span class="contact-icon">
          <svg viewBox="0 0 24 24" fill="#ffffff"><path d="M6.6 10.8a15.1 15.1 0 0 0 6.6 6.6l2.2-2.2c.3-.3.7-.4 1-.2 1.1.4 2.3.6 3.6.6.6 0 1 .4 1 1V20c0 .6-.4 1-1 1C10.6 21 3 13.4 3 4c0-.6.4-1 1-1h3.5c.6 0 1 .4 1 1 0 1.3.2 2.5.6 3.6.1.3 0 .7-.2 1L6.6 10.8z"/></svg>
        </span>
        <span>+1 720 555 0147</span>
      </div>

      <div class="contact contact-email">
        <span class="contact-icon">
          <svg viewBox="0 0 24 24" fill="none" stroke="#ffffff" stroke-width="2"><rect x="3" y="5" width="18" height="14" rx="1"/><path d="M3 6l9 7 9-7"/></svg>
        </span>
        <span>email@quorvanecapital.example</span>
      </div>

      <div class="contact contact-mobile">
        <span class="contact-icon">
          <svg viewBox="0 0 24 24" fill="none" stroke="#ffffff" stroke-width="2"><rect x="7" y="2" width="10" height="20" rx="2"/><path d="M11 18h2"/></svg>
        </span>
        <span>+1 720 555 0198</span>
      </div>

      <div class="brand">
        <span class="brand-square"></span>
        <span class="brand-name">Quorvane Capital</span>
      </div>

      <svg class="accent-band" viewBox="0 0 170 9" preserveAspectRatio="none">
        <polygon points="9,0 170,0 170,9 0,9" fill="var(--accent)"/>
      </svg>
    </section>
  </main>
</body>
</html>
```